Gardener needs an exciting new flyer design.

I'm a passionate gardener that requires a custom flyer design for a owner operator gardening business. Design will be for a DL flyer. I'm based on the Sunshine coast in Queensland Australia. My target audience is the residential market on the Sunshine coast. Business name is Marlowe Greens. My services are, lawn mowing, weeding, Eco Friendly fertilizing, green waste removal, Mulching, tree and shrub pruning, Full garden makeovers, hedging, pressure cleaning, privacy screening, Timber deck rejuvenation, Planting, Turf preparation and installation, and much more. Free no obligation quotes, reliable and friendly service, great rates. 12 years experience. Web www.marlowegreens.com.au - Phone 0418527064 - Email doug@marlowegreens.com.au I would like the design to portray a friendly and professional approach.

Target Market(s)

Residential

Industry/Entity Type

Gardener

Font styles to use
Serif

Colors
9ccb3b
abd037
3176b5

Requirements
Must have
• my services, my logo, my contact details,

```html
<!DOCTYPE html>
<html lang="en">
<head>
<meta charset="utf-8">
<title>Marlowe Greens – DL Flyer</title>
<link rel="stylesheet" href="https://fonts.googleapis.com/css2?family=Kaushan+Script&family=Lato:wght@400;700;900&display=swap">
<style>
  :root{
    --page:#ebebeb;
    --paper:#ffffff;
    --leaf:#7dc242;
    --leaf-bright:#9ccb3b;
    --forest:#1e7a35;
    --ink-green:#2e7d1e;
    --text:#111111;
    --accent:#6b3f8f;
  }
  *{margin:0;padding:0;box-sizing:border-box}
  html,body{width:1200px;height:794px;overflow:hidden;background:var(--page);font-family:'Lato',sans-serif;color:var(--text)}
  .flyer{position:absolute;top:39px;width:340px;height:716px;background:var(--paper);box-shadow:0 2px 6px rgba(0,0,0,.08)}
  .flyer--front{left:240px}
  .flyer--back{left:620px}
  .block{position:absolute}
  .photo{position:absolute}

  /* front */
  .promo{left:15px;top:15px;width:173px;height:233px;background:var(--leaf);padding:40px 8px 0 12px}
  .promo__headline{font-family:'Kaushan Script',cursive;font-weight:400;color:var(--ink-green);font-size:25px;line-height:33px;white-space:nowrap}
  .promo__intro{margin-top:16px;font-size:7.5px;line-height:9.5px;font-weight:700;color:#1a3a10}
  .brand{left:150px;top:535px;width:180px;display:flex;align-items:center;gap:6px}
  .brand__mark{width:12px;height:12px;background:var(--forest)}
  .brand__name{font-family:'Lato',sans-serif;font-weight:900;font-size:17px;color:var(--forest)}
  .contact-tab{left:15px;top:597px;width:57px;height:101px;background:var(--leaf)}
  .contact-card{left:80px;top:597px;width:239px;height:101px;background:var(--forest);border-top:3px solid var(--leaf);border-bottom:3px solid var(--leaf);padding:12px 0 0 18px;color:#fff}
  .contact-card__title{font-size:15px;font-weight:700;display:inline-block;border-bottom:2px solid #fff;padding-bottom:1px;margin-bottom:6px}
  .contact-card__phone{font-size:14px;line-height:17px}
  .contact-card__line{font-size:11.5px;line-height:15px}
  .contact-card__line--email{font-size:13.5px;line-height:18px}

  /* back */
  .owner-title{left:219px;top:76px;font-family:'Kaushan Script',cursive;color:var(--ink-green);font-size:27px;line-height:34px;text-transform:uppercase;letter-spacing:.5px}
  .owner-name{left:219px;top:182px;font-size:14px;font-weight:700}
  .owner-bio{left:219px;top:206px;width:112px;font-size:9.5px;line-height:11.6px}
  .owner-bio__offer{display:block;margin-top:4px;font-weight:700;color:var(--ink-green)}
  .services-title{left:16px;top:372px;font-family:'Kaushan Script',cursive;color:var(--ink-green);font-size:27px}
  .services{left:24px;top:407px;list-style:none}
  .services li{font-size:9.5px;line-height:14.5px;position:relative;padding-left:10px}
  .services li::before{content:"";position:absolute;left:0;top:5px;width:4px;height:4px;background:var(--leaf-bright)}
  .contact{left:17px;top:630px}
  .contact__title{color:var(--ink-green);font-size:13px;font-weight:900;display:inline-block;border-bottom:2px solid var(--accent);margin-bottom:6px}
  .contact__phone{font-size:13px;line-height:15px}
  .contact__line{font-size:10.5px;line-height:13px}
  .contact__line--email{font-size:12px;line-height:16px}
  .badge{left:213px;top:625px;width:109px;height:72px;background:var(--leaf);display:flex;align-items:flex-end;justify-content:center;padding-bottom:10px}
  .badge__name{font-family:'Lato',sans-serif;font-weight:900;font-size:11.5px;color:#fff}
</style>
</head>
<body>

<section class="flyer flyer--front">
  <div class="block promo">
    <h1 class="promo__headline">We can help<br>to make your<br>garden more<br>beautiful</h1>
    <p class="promo__intro">I'm a passionate gardener based on the Sunshine coast in Queensland Australia.</p>
  </div>
  <div class="photo" role="img" aria-label="Photo of a pot of marigolds with a red trowel on soil" style="left:203px;top:15px;width:120px;height:368px;background:linear-gradient(180deg,#7aa64a 0%,#c9a13c 30%,#c4412a 45%,#8a6a45 70%,#6b5a48 100%)"></div>
  <div class="photo" role="img" aria-label="Photo of a garden patio with wicker furniture among trees" style="left:15px;top:266px;width:173px;height:117px;background:linear-gradient(180deg,#3f6b2c 0%,#6c8a45 45%,#a68c6a 75%,#8a6e52 100%)"></div>
  <div class="photo" role="img" aria-label="Decorative corner of green swirls with butterflies" style="left:20px;top:395px;width:230px;height:187px;background:radial-gradient(ellipse at 30% 35%,#bfe28a 0%,#e4f3cf 45%,#ffffff 75%)"></div>
  <div class="block brand">
    <span class="brand__mark"></span>
    <span class="brand__name">Marlowe Greens</span>
  </div>
  <div class="block contact-tab"></div>
  <div class="block contact-card">
    <h2 class="contact-card__title">CONTACT US</h2>
    <p class="contact-card__phone">0418527064</p>
    <p class="contact-card__line">www.marlowegreens.com.au</p>
    <p class="contact-card__line contact-card__line--email">doug@marlowegreens.com.au</p>
  </div>
</section>

<section class="flyer flyer--back">
  <div class="photo" role="img" aria-label="Photo of a parent and child watering seedlings in a wooden crate" style="left:17px;top:17px;width:188px;height:344px;background:linear-gradient(180deg,#6b3f24 0%,#8a5534 40%,#b5473a 60%,#c9a777 85%,#a58655 100%)"></div>
  <h2 class="block owner-title">Meet<br>the<br>owner</h2>
  <p class="block owner-name">Doug Marlowe</p>
  <p class="block owner-bio">From the beautiful Sunshine coast. Doug has over 12 years of experience in gardening and lawn care. With a deep passion in Horticulture you know your in the right hands.<span class="owner-bio__offer">Free no obligation quotes.</span></p>

  <h2 class="block services-title">Our Services</h2>
  <ul class="block services">
    <li>Lawn Mowing</li>
    <li>Weeding</li>
    <li>Eco Friendly Fertilizing</li>
    <li>Green Waste Removal</li>
    <li>Mulching</li>
    <li>Tree and shrub pruning</li>
    <li>Full garden makeovers</li>
    <li>Hedging</li>
    <li>Pressure cleaning</li>
    <li>Privacy screening</li>
    <li>Timber deck rejuvenation</li>
    <li>Planting</li>
    <li>Turf preparation and installation</li>
    <li>and much more</li>
  </ul>
  <div class="photo" role="img" aria-label="Photo of a gardener harvesting vegetables in a rooftop garden" style="left:213px;top:373px;width:109px;height:238px;background:linear-gradient(180deg,#c9d3d8 0%,#6f9a4a 35%,#4d7a33 65%,#3c5e2a 100%)"></div>

  <div class="block contact">
    <h2 class="contact__title">CONTACT US</h2>
    <p class="contact__phone">0418527064</p>
    <p class="contact__line">www.marlowegreens.com.au</p>
    <p class="contact__line contact__line--email">doug@marlowegreens.com.au</p>
  </div>
  <div class="block badge"><span class="badge__name">Marlowe Greens</span></div>
</section>

</body>
</html>
```